Family Medicine Clinic Needs Mailchimp Newsletter Template

Looking for a responsive mailchimp template that matches the theme and overall look/feel of our website brookvaleclinic.com.

I'm looking for a professional, clean, simple, minimalist, bold design.
Colors would ideally be greens and blues, cool tones, muted colors, or graytones.

See attached word document for content for the upcoming newsletter

Can see prior newsletter content here:
http://brookvaleclinic.com/ourresources/newsletter-archive/

I have attached a copy of our brochure to see a sample of what we offer

The desired newsletter title would be:
The Brook Note
Looking for a great banner for that

Looking for basically 1 main photo area per text area for future templates

Under September is Spine Focus Season want links to our different services I mention

Under the videos section would like a video gallery of sorts that have links to the videos

Lumaderm image ad needs to be redone

Would like a button to take to schedule an appointment and patient portal
Easily visible phone number
Would like to have several sections with buttons to find out more

Would like feedback question at bottom
Rated 7-10 would forward to
https://lnkvo.net/qX8pZa

1-6 would send email to us

Reason: I have now guaranteed payment so I am giving a few more days for those designers that still want to submit a design

Clinic

Coded - Design and coding required

```html
<!DOCTYPE html>
<html lang="en">
<head>
<meta charset="utf-8">
<title>The Brook Note – Brookvale Clinic Newsletter</title>
<link rel="stylesheet" href="https://fonts.googleapis.com/css2?family=Open+Sans:wght@400;600;700;800&display=swap">
<style>
  :root {
    --blue: #2f9fd8;
    --blue-dark: #1f6f9f;
    --title-blue: #23709f;
    --green: #7cb534;
    --green-dark: #5f9a22;
    --grey-bg: #f2f2f2;
    --text: #444;
    --muted: #777;
    --white: #fff;
  }
  * { box-sizing: border-box; margin: 0; padding: 0; }
  html, body { width: 1200px; height: 3136px; overflow: hidden; background: var(--white); }
  body { font-family: "Open Sans", Arial, sans-serif; color: var(--text); position: relative; }
  section, header, footer { position: relative; width: 1200px; }
  .abs { position: absolute; }

  .btn {
    position: absolute; left: 50%; transform: translateX(-50%);
    width: 166px; height: 44px; border-radius: 22px;
    background: linear-gradient(var(--green), var(--green-dark));
    color: var(--white); font-size: 13px; font-weight: 700; letter-spacing: .5px;
    display: flex; align-items: center; justify-content: center; text-transform: uppercase;
  }
  .btn--white { background: var(--white); color: var(--text); }

  .section-title { position: absolute; left: 0; width: 100%; text-align: center; font-size: 33px; font-weight: 700; }

  /* Header */
  .site-header { height: 116px; border-top: 4px solid var(--blue); }
  .brand { position: absolute; left: 75px; top: 30px; display: flex; align-items: center; gap: 12px; }
  .brand__mark { width: 40px; height: 40px; border-radius: 50%; background: var(--green); }
  .brand__name { font-size: 30px; font-weight: 700; color: var(--title-blue); }
  .portal-tab {
    position: absolute; left: 857px; top: 0; width: 251px; height: 46px;
    background: linear-gradient(var(--blue), var(--blue-dark)); border-radius: 0 0 22px 22px;
    color: var(--white); font-size: 14px; font-weight: 700; letter-spacing: .5px;
    display: flex; align-items: center; justify-content: center; gap: 8px;
  }
  .schedule-btn {
    position: absolute; left: 497px; top: 62px; width: 270px; height: 44px; border-radius: 22px;
    background: linear-gradient(var(--green), var(--green-dark)); color: var(--white);
    font-size: 14px; font-weight: 700; letter-spacing: .5px; display: flex; align-items: center; justify-content: center;
  }
  .call { position: absolute; left: 800px; top: 66px; display: flex; align-items: center; gap: 10px; font-size: 17px; font-weight: 600; color: #333; }
  .call__number { font-size: 23px; font-weight: 700; color: var(--title-blue); }

  /* Hero */
  .hero { height: 510px; overflow: hidden; }
  .hero__photo { position: absolute; inset: 0; background: linear-gradient(100deg, #5aa6e6 0%, #8cc4f0 45%, #cfe6f7 70%, #e9d8c9 100%); }
  .hero__title {
    position: absolute; left: 78px; top: 290px; transform: translateY(-50%);
    font-size: 72px; font-weight: 800; color: var(--white);
    text-shadow: 0 3px 0 #1b4f7a, 0 0 6px rgba(0,0,0,.35);
  }

  /* Awareness */
  .awareness { height: 365px; }
  .awareness .section-title { top: 38px; color: var(--title-blue); }
  .awareness__sub { position: absolute; top: 98px; width: 100%; text-align: center; font-size: 22px; font-weight: 600; color: #333; }
  .facts { position: absolute; top: 156px; left: 162px; display: flex; gap: 40px; }
  .fact { width: 420px; display: flex; gap: 14px; font-size: 15px; line-height: 27px; color: #555; }
  .fact svg { flex: none; margin-top: 5px; }
  .awareness .btn { top: 276px; }

  /* Services */
  .services { height: 525px; background: var(--blue); color: var(--white); }
  .services .section-title { top: 38px; color: var(--white); }
  .service { position: absolute; width: 260px; margin-left: -130px; text-align: center; font-size: 16px; font-weight: 700; line-height: 22px; }
  .service svg { display: block; margin: 0 auto 12px; }
  .services .btn { top: 427px; }

  /* Video */
  .video { height: 626px; }
  .video .section-title { top: 38px; color: var(--title-blue); }
  .video__main { position: absolute; left: 256px; top: 112px; width: 693px; height: 336px; border: 4px solid #ddd;
    background: linear-gradient(180deg, #9aa1a6 0%, #8a7566 45%, #6b6660 70%, #545454 100%); }
  .play { position: absolute; left: 50%; top: 50%; transform: translate(-50%, -50%); }
  .thumb { position: absolute; top: 462px; width: 219px; height: 112px; border: 4px solid #ddd; }
  .thumb--1 { left: 256px; background: linear-gradient(135deg, #b8b6ae, #d8d4c6 60%, #7cb534 100%); }
  .thumb--2 { left: 491px; background: linear-gradient(135deg, #e7d9a6, #efe6c5 60%, #7cb534 100%); }
  .thumb--3 { left: 731px; background: linear-gradient(135deg, #c9c7c4, #e3e1dd 60%, #7cb534 100%); }
  .arrow { position: absolute; }

  /* Before & After */
  .results { height: 416px; background: var(--grey-bg); }
  .results .section-title { top: 36px; color: var(--title-blue); }
  .pair { position: absolute; top: 101px; width: 331px; }
  .pair__photos { display: flex; gap: 4px; height: 147px; }
  .pair__photos div { flex: 1; background: linear-gradient(160deg, #e8c4a6, #c99a7c 60%, #b48469); }
  .pair__labels { display: flex; gap: 4px; height: 40px; }
  .pair__labels span { flex: 1; background: var(--blue); color: var(--white); font-size: 13px; font-weight: 700; display: flex; align-items: center; justify-content: center; }
  .results .btn { top: 316px; }

  /* Feedback */
  .feedback { height: 378px; background: var(--green); color: var(--white); }
  .feedback .section-title { top: 44px; color: var(--white); }
  .review { position: absolute; top: 112px; width: 330px; }
  .review__rating { display: flex; align-items: center; gap: 3px; font-size: 14px; font-weight: 700; color: #ffe34d; margin-bottom: 10px; }
  .review__rating b { margin-left: 12px; font-weight: 700; }
  .review p { font-size: 14.5px; line-height: 24px; }
  .feedback .btn { top: 291px; }

  /* Footer */
  .site-footer { height: 200px; text-align: center; }
  .site-footer .brand { position: absolute; left: 50%; top: 38px; transform: translateX(-50%); }
  .copyright { position: absolute; top: 110px; width: 100%; font-size: 13px; color: var(--muted); }
  .social { position: absolute; top: 144px; left: 50%; transform: translateX(-50%); display: flex; gap: 20px; }
  .social span { width: 20px; height: 20px; border-radius: 50%; background: #555; }
</style>
</head>
<body>

<header class="site-header">
  <div class="brand"><span class="brand__mark"></span><span class="brand__name">Brookvale Clinic</span></div>
  <div class="portal-tab">
    <svg width="14" height="14" viewBox="0 0 14 14"><circle cx="7" cy="4" r="3.2" fill="#fff"/><path d="M1 14c0-4 3-6 6-6s6 2 6 6z" fill="#fff"/></svg>
    PATIENT PORTAL
  </div>
  <div class="schedule-btn">SCHEDULE AN APPOINTMENT</div>
  <div class="call">
    <svg width="20" height="20" viewBox="0 0 24 24"><path d="M6.6 10.8a15 15 0 0 0 6.6 6.6l2.2-2.2a1 1 0 0 1 1-.25 11.4 11.4 0 0 0 3.6.57 1 1 0 0 1 1 1V20a1 1 0 0 1-1 1A17 17 0 0 1 3 4a1 1 0 0 1 1-1h3.5a1 1 0 0 1 1 1c0 1.25.2 2.45.57 3.57a1 1 0 0 1-.25 1z" fill="#333"/></svg>
    CALL US NOW: <span class="call__number">(555) 214-7380</span>
  </div>
</header>

<section class="hero">
  <div class="hero__photo" role="img" aria-label="Smiling couple embracing outdoors under a bright blue sky"></div>
  <h1 class="hero__title">The Brook Note</h1>
</section>

<section class="awareness">
  <h2 class="section-title">September is Spine Focus Season</h2>
  <p class="awareness__sub">What You Need to Know</p>
  <div class="facts">
    <div class="fact">
      <svg width="16" height="16" viewBox="0 0 16 16"><circle cx="8" cy="8" r="8" fill="var(--green)"/><path d="M4.5 8.2l2.3 2.3 4.7-4.8" stroke="#fff" stroke-width="2" fill="none"/></svg>
      <p>Nearly 100 million Americans experience chronic pain more than those who have diabetes, heart disease and cancer combined..</p>
    </div>
    <div class="fact">
      <svg width="16" height="16" viewBox="0 0 16 16"><circle cx="8" cy="8" r="8" fill="var(--green)"/><path d="M4.5 8.2l2.3 2.3 4.7-4.8" stroke="#fff" stroke-width="2" fill="none"/></svg>
      <p>Pain is a warning sign that indicates a problem that needs attention, don't just mask your symptoms, let us help try to get to the root of your issue.</p>
    </div>
  </div>
  <div class="btn">View More</div>
</section>

<section class="services">
  <h2 class="section-title">Our Services</h2>

  <div class="service" style="left:195px;top:112px">
    <svg width="56" height="56" viewBox="0 0 56 56" fill="none" stroke="#fff" stroke-width="4"><path d="M28 6v46"/><path d="M8 14c8 0 12 4 20 4s12-4 20-4"/><path d="M20 26c8 4 8 8 0 12M36 26c-8 4-8 8 0 12"/></svg>
    Integrative Family Medicine
  </div>
  <div class="service" style="left:466px;top:112px">
    <svg width="56" height="56" viewBox="0 0 56 56" fill="none" stroke="#fff" stroke-width="4"><circle cx="28" cy="18" r="13"/><path d="M28 31v20M16 51h24"/></svg>
    Functional Medicine
  </div>
  <div class="service" style="left:739px;top:112px">
    <svg width="56" height="56" viewBox="0 0 56 56"><path d="M12 12h24v10H12z" fill="none" stroke="#fff" stroke-width="4"/><path d="M10 22h28v28H10z" fill="none" stroke="#fff" stroke-width="4"/><circle cx="40" cy="40" r="12" fill="#fff"/></svg>
    Nutrition
  </div>
  <div class="service" style="left:1008px;top:112px">
    <svg width="56" height="56" viewBox="0 0 56 56" fill="none" stroke="#fff" stroke-width="4"><circle cx="28" cy="12" r="5"/><path d="M12 6l16 18 16-18M28 24v26M6 36h10M40 36h10"/></svg>
    Weight Loss
  </div>

  <div class="service" style="left:195px;top:252px">
    <svg width="56" height="56" viewBox="0 0 56 56" fill="#fff"><circle cx="20" cy="14" r="6"/><rect x="6" y="28" width="44" height="8" rx="2"/><rect x="10" y="36" width="4" height="14"/><rect x="42" y="36" width="4" height="14"/></svg>
    Osteopathic Manipulation
  </div>
  <div class="service" style="left:466px;top:252px">
    <svg width="56" height="56" viewBox="0 0 56 56" fill="#fff"><circle cx="14" cy="24" r="6"/><rect x="4" y="32" width="48" height="8" rx="2"/><rect x="8" y="40" width="4" height="12"/><rect x="44" y="40" width="4" height="12"/><rect x="28" y="8" width="3" height="20"/><rect x="36" y="10" width="3" height="18"/></svg>
    Acupuncture
  </div>
  <div class="service" style="left:739px;top:252px">
    <svg width="56" height="56" viewBox="0 0 56 56" fill="none" stroke="#fff" stroke-width="4"><circle cx="24" cy="32" r="11"/><path d="M24 43v10M18 49h12M32 24l14-14M36 10h10v10"/></svg>
    Bio-Identical Hormone<br>Replacement
  </div>
  <div class="service" style="left:1008px;top:252px">
    <svg width="56" height="56" viewBox="0 0 56 56" fill="none" stroke="#fff" stroke-width="4"><path d="M22 6h12M24 6v16L10 48h36L32 22V6"/><circle cx="30" cy="38" r="3" fill="#fff"/></svg>
    Labs
  </div>

  <div class="btn">View More</div>
</section>

<section class="video">
  <h2 class="section-title">Video Gallery</h2>
  <svg class="arrow" style="left:206px;top:266px" width="20" height="32" viewBox="0 0 20 32"><path d="M16 2L4 16l12 14" stroke="#aaa" stroke-width="4" fill="none"/></svg>
  <div class="video__main" role="img" aria-label="Clinic building exterior with entrance and signage">
    <svg class="play" width="64" height="64" viewBox="0 0 64 64"><circle cx="32" cy="32" r="28" fill="none" stroke="#fff" stroke-width="5"/><path d="M26 19l20 13-20 13z" fill="#fff"/></svg>
  </div>
  <svg class="arrow" style="left:974px;top:266px" width="20" height="32" viewBox="0 0 20 32"><path d="M4 2l12 14L4 30" stroke="#aaa" stroke-width="4" fill="none"/></svg>
  <div class="thumb thumb--1" role="img" aria-label="Video thumbnail: physician speaking in the clinic"></div>
  <div class="thumb thumb--2" role="img" aria-label="Video thumbnail: staff member in a hallway"></div>
  <div class="thumb thumb--3" role="img" aria-label="Video thumbnail: patient testimonial"></div>
</section>

<section class="results">
  <h2 class="section-title">Before &amp; After</h2>
  <svg class="arrow" style="left:42px;top:160px" width="16" height="28" viewBox="0 0 16 28"><path d="M13 2L3 14l10 12" stroke="#aaa" stroke-width="3.5" fill="none"/></svg>
  <div class="pair" style="left:76px">
    <div class="pair__photos" role="img" aria-label="Eye area skin before and after treatment"><div></div><div></div></div>
    <div class="pair__labels"><span>Before</span><span>After</span></div>
  </div>
  <div class="pair" style="left:435px">
    <div class="pair__photos" role="img" aria-label="Facial skin before and after treatment"><div></div><div></div></div>
    <div class="pair__labels"><span>Before</span><span>After</span></div>
  </div>
  <div class="pair" style="left:800px">
    <div class="pair__photos" role="img" aria-label="Forehead lines before and after treatment"><div></div><div></div></div>
    <div class="pair__labels"><span>Before</span><span>After</span></div>
  </div>
  <svg class="arrow" style="left:1143px;top:160px" width="16" height="28" viewBox="0 0 16 28"><path d="M3 2l10 12L3 26" stroke="#aaa" stroke-width="3.5" fill="none"/></svg>
  <div class="btn">View More</div>
</section>

<section class="feedback">
  <h2 class="section-title">Feedback Questions</h2>
  <div class="review" style="left:76px">
    <div class="review__rating">★★★★★★★ <b>7/10</b></div>
    <p>Lorem ipsum dolor sit amet, consect- etuer adipiscing elit, sed diam nonummy nibh euismod tincidunt ut laoreet dolore magna aliquam erat volutpat.</p>
  </div>
  <div class="review" style="left:437px">
    <div class="review__rating">★★★★★★★ <b>7/10</b></div>
    <p>Lorem ipsum dolor sit amet, consect- etuer adipiscing elit, sed diam nonummy nibh euismod tincidunt ut laoreet dolore magna aliquam erat volutpat.</p>
  </div>
  <div class="review" style="left:800px">
    <div class="review__rating">★★★★★★★ <b>7/10</b></div>
    <p>Lorem ipsum dolor sit amet, consect- etuer adipiscing elit, sed diam nonummy nibh euismod tincidunt ut laoreet dolore magna aliquam erat volutpat.</p>
  </div>
  <div class="btn btn--white">View More</div>
</section>

<footer class="site-footer">
  <div class="brand"><span class="brand__mark"></span><span class="brand__name">Brookvale Clinic</span></div>
  <p class="copyright">Copyright © 2017. Company Name. All Rights Reserved.</p>
  <div class="social" aria-label="Social links"><span></span><span></span><span></span><span></span><span></span></div>
</footer>

</body>
</html>
```